Website for Painting Company

Hi,
We are after a Wordpress website design with CSS/HTML Theme for our painting company based in Brisbane, Australia. Our business name is Felix Morrow Painting Contractors and we have been trading for 33 years.
We want a website that is modern and fresh with a professional image. Our organisation does Commercial, Residential and Insurance Painting projects. I have listed a couple of similar websites that we like the look and feel of. These are a guide only and we are happy to see you own designs with a similar professional image.
http://www.kelbrookcoatings.com.au/
http://www.tidewellfinishes.com.au/
We are a member of Guild Decorators Australia and I have supplied the logo named "gda" which I have included in the files I have uploaded.
We want a five page site. These are Home Page, Residential, Commercial, Insurance and Contact Us.
I have also uploaded our logo and some pictures labeled Logo,Residential, Commercial, Insurance and Homepage. These should be used on each page listed above.
Updates
Project Deadline Extended
Reason: We are extending because we need more time to go through the designs and give feedback. There are many fantastic designs. Thank you everyone who has contributed!!!!
All the best
Derek
Industry/Entity Type
Painting
Requirements
Must have
- We want a five page site. These are Home Page, Residential, Commercial, Insurance and Contact Us.

```html
<!DOCTYPE html>
<html lang="en">
<head>
<meta charset="utf-8">
<title>Felix Morrow Painting Contractors</title>
<link href="https://fonts.googleapis.com/css2?family=Ubuntu:wght@400;500;700&family=Arimo:wght@400&display=swap" rel="stylesheet">
<style>
:root{
  --red:#c0000d;
  --red-dark:#9a0008;
  --ink:#4a4a4a;
  --ink-soft:#777;
  --page:#f1f1f1;
  --outer:#e6e6e6;
  --side:#e8e8e8;
  --rule:#c9c9c9;
  --nav:#6c6c6c;
  --footer:#2b2b2b;
  --plum:#a0003a;
  --photo-a:#d9cfc3;
  --photo-b:#8d7e6e;
}
*{box-sizing:border-box;margin:0;padding:0}
html,body{width:1029px;height:1200px;overflow:hidden}
body{background:var(--outer);font-family:"Ubuntu",sans-serif;color:var(--ink);position:relative}
.abs{position:absolute}
.topnav{left:0;top:0;width:1029px;height:31px;background:linear-gradient(#7a7a7a,#5f5f5f)}
.topnav a{position:absolute;top:0;height:31px;line-height:31px;color:#fff;font-size:11.5px;font-weight:500;text-decoration:none;transform:translateX(-50%)}
.topnav .active{left:96px;width:100px;transform:none;text-align:center;background:linear-gradient(#e0101c,#b8000b);height:36px;line-height:31px}
.topnav .sep{position:absolute;top:3px;width:1px;height:25px;border-left:1px dotted #999}
.page{left:87px;top:31px;width:855px;height:1109px;background:var(--page)}
.brand{left:110px;top:56px}
.brand .mark{width:14px;height:14px;background:var(--red);position:absolute;left:0;top:6px}
.brand .name{position:absolute;left:22px;top:0;width:130px;color:var(--red);font-weight:700;font-size:21px;line-height:24px}
.contact{right:96px;text-align:right}
.call{top:40px;font-size:16px;font-weight:700;color:var(--red)}
.call span{color:var(--ink-soft)}
.follow{top:84px;display:flex;align-items:center;gap:9px;font-size:12px;font-weight:700;color:#666;letter-spacing:1px}
.follow i{display:block;width:24px;height:24px;background:#8a8a8a;border-radius:3px}
.addr{top:131px;font-size:11.5px;font-weight:700;color:#333}
.addr span{font-weight:400;color:var(--ink-soft)}
.mail{top:149px;font-size:11px;color:var(--ink-soft)}
.mail span{color:var(--red);font-weight:700}
.slider{left:98px;top:179px;width:835px;height:355px;background:#d6d6d6;border:1px solid #c4c4c4}
.slide{left:10px;top:10px;width:812px;height:333px;background:linear-gradient(100deg,var(--photo-a) 0%,#ece6dc 45%,#b9a893 70%,var(--photo-b) 100%)}
.thumb{top:245px;width:134px;height:92px;background:#fff;padding:6px}
.thumb div{width:100%;height:100%}
.intro{left:99px;top:560px;width:556px}
.intro h1{font-size:21px;font-weight:700;color:#555}
.intro h1 b{color:var(--red)}
.intro p{font-size:9.5px;line-height:17px;margin-top:12px;text-align:justify;color:#555}
.intro p strong{color:var(--red)}
.intro p+p{margin-top:17px}
.blogs{left:99px;top:749px;width:571px;height:373px;background:#f6f6f6;border:1px solid #e2e2e2}
.blogs h2{position:absolute;left:56px;top:18px;font-size:19px;font-weight:700;color:#555}
.blogs h2 b{color:var(--red)}
.flag{left:103px;top:755px}
.post{left:75px;width:580px}
.date{position:absolute;left:0;top:0;width:36px;text-align:center;font-family:"Arimo",sans-serif}
.date .m,.date .y{background:#a9a9a9;color:#fff;font-size:10px;height:17px;line-height:17px}
.date .d{background:#e9555a;color:#fff;font-size:20px;font-weight:700;height:28px;line-height:28px}
.post h3{position:absolute;font-size:14px;font-weight:400;color:var(--plum);white-space:nowrap}
.post .meta{position:absolute;font-size:10.5px;color:#888}
.post .body{position:absolute;font-size:9px;line-height:15.5px;color:#555}
.post .by{position:absolute;font-family:"Arimo",sans-serif;font-size:10.5px;color:var(--plum)}
.post .by span{color:#777}
.post .share{position:absolute;font-family:"Arimo",sans-serif;font-size:10.5px;color:#777;display:flex;align-items:center;gap:3px}
.post .share i{display:block;width:14px;height:14px;background:#bbb;border:1px solid #999;margin-left:1px}
.post .share em{font-style:normal;margin-right:4px}
.post .more{position:absolute;font-family:"Arimo",sans-serif;font-size:10.5px;color:var(--plum)}
.sidebar{left:690px;top:540px;width:252px;height:600px;background:var(--side)}
.side h2{position:absolute;left:704px;font-size:17px;font-weight:700;color:#555}
.cats{left:708px;top:602px;width:206px;list-style:none}
.cats li{height:26px;border-bottom:1px dotted var(--rule);font-size:9.5px;line-height:26px;color:#333;padding-left:23px;position:relative}
.cats li::before{content:"";position:absolute;left:10px;top:10px;width:5px;height:5px;background:var(--red)}
.member{left:723px;top:843px;font-size:14px;font-weight:700;font-style:italic;color:#1f2f9a}
.badge{left:712px;top:870px;width:197px;height:146px}
.cards{left:725px;width:190px;display:flex;justify-content:space-between}
.cards i{display:block;height:20px;background:#cfcfcf;border:1px solid #b5b5b5;border-radius:2px}
.footer{left:0;top:1140px;width:1029px;height:60px;background:linear-gradient(#3a3a3a,#1f1f1f)}
.footer a{position:absolute;top:27px;color:#fff;font-size:11.5px;text-decoration:none;transform:translateX(-50%)}
.footer .bar{position:absolute;top:28px;width:1px;height:12px;background:#ccc}
</style>
</head>
<body>

<nav class="abs topnav">
  <a class="active" href="#">Home Page</a>
  <span class="sep" style="left:211px"></span>
  <a href="#" style="left:268px">Residential</a>
  <span class="sep" style="left:331px"></span>
  <a href="#" style="left:393px">Commercial</a>
  <span class="sep" style="left:457px"></span>
  <a href="#" style="left:513px">Insurance</a>
  <span class="sep" style="left:571px"></span>
  <a href="#" style="left:630px">Contact Us</a>
</nav>

<div class="abs page"></div>

<header>
  <div class="abs brand">
    <span class="mark"></span>
    <div class="name">Felix Morrow Painting Contractor</div>
  </div>
  <div class="abs contact call">Call the team <span>(08) 9412 7780</span></div>
  <div class="abs contact follow">FOLLOW US ON <i></i><i></i><i></i><i></i></div>
  <div class="abs contact addr">Address: <span>PO Box 318, Ashvale, 6972</span></div>
  <div class="abs contact mail">Email: <span>info@tidewellfinishes.com.au</span></div>
</header>

<section class="abs slider">
  <div class="abs slide" role="img" aria-label="Photo of a bright open-plan living and dining room"></div>
  <div class="abs thumb" style="left:396px"><div role="img" aria-label="Interior with a timber staircase" style="background:linear-gradient(135deg,#d8cdbd,#6f5b45)"></div></div>
  <div class="abs thumb" style="left:539px"><div role="img" aria-label="Warm lounge room with fireplace" style="background:linear-gradient(135deg,#e9c98f,#9a6a3a)"></div></div>
  <div class="abs thumb" style="left:681px"><div role="img" aria-label="Modern white house under blue sky" style="background:linear-gradient(180deg,#3d79c8 0%,#9ec0e6 55%,#e9e9e9 75%,#6e7f4e 100%)"></div></div>
</section>

<main>
  <section class="abs intro">
    <h1><b>Painters</b> Brisbane</h1>
    <p><strong>Kelbrook Painters (Brisbane, Queensland, Qld) Above &amp; Beyond are dedicated to providing the highest quality painting work with the best possible service to our customers.</strong> We pride ourselves on quality workmanship from our qualified Brisbane Painters and we understand the importance of professionalism and friendly service.</p>
    <p>With Kelbrook Painters Above &amp; Beyond you get a quality experience that is unique in the painting business, going above and beyond the basic painting services - and you will get all this experience at competitive prices by professional Brisbane Painters in Queensland.</p>
  </section>

  <section class="abs blogs"><h2><b>Recent</b> Blogs</h2></section>
  <svg class="abs flag" width="46" height="46" viewBox="0 0 46 46" aria-hidden="true">
    <line x1="6" y1="44" x2="14" y2="4" stroke="#888" stroke-width="2"/>
    <path d="M14 4 L44 12 L36 34 L9 28 Z" fill="#d8321e"/>
    <rect x="22" y="13" width="10" height="10" rx="2" fill="#fff"/>
  </svg>

  <article class="abs post" style="top:827px">
    <div class="date"><div class="m">March</div><div class="d">16</div><div class="y">2012</div></div>
    <h3 style="left:56px;top:-10px">The inside scoop from Tidewell Finishing Contracts</h3>
    <div class="meta" style="left:60px;top:9px">Posted on September 15, 2011 by admin</div>
    <p class="body" style="left:60px;top:28px;width:513px">Lorem Ipsum is simply dummy text of the printing and typesetting industry. Lorem Ipsum has been the industry's standard dummy text ever since the 1500s, when an unknown printer took a galley of type and scrambled it to make a type specimen book. It has survived not only five centuries, but also the leap into electronic typesetting, remaining essentially unchanged. Lorem Ipsum is simply dummy text of the printing and typesetting industry.</p>
    <div class="by" style="left:60px;top:103px">[Blog Psted By <span>Owen Marsh</span>]</div>
    <div class="share" style="left:61px;top:119px"><em>Share This</em><i></i><i></i><i></i><i></i></div>
    <a class="more" style="left:506px;top:122px">More info</a>
  </article>

  <article class="abs post" style="top:999px">
    <div class="date"><div class="m">March</div><div class="d">16</div><div class="y">2012</div></div>
    <h3 style="left:49px;top:-10px">The inside scoop from Tidewell Finishing Contracts</h3>
    <div class="meta" style="left:51px;top:7px">Posted on September 15, 2011 by admin</div>
    <p class="body" style="left:51px;top:25px;width:512px">Lorem Ipsum is simply dummy text of the printing and typesetting industry. Lorem Ipsum has been the industry's standard dummy text ever since the 1500s, when an unknown printer took a galley of type and scrambled it to make a type specimen book. It has survived not only five</p>
    <div class="by" style="left:51px;top:78px">[Blog Psted By <span>Owen Marsh</span>]</div>
    <div class="share" style="left:52px;top:102px"><em>Share This</em><i></i><i></i><i></i><i></i></div>
    <a class="more" style="left:497px;top:104px">More info</a>
  </article>
</main>

<aside class="side">
  <div class="abs sidebar"></div>
  <h2 style="top:567px">Categories</h2>
  <ul class="abs cats">
    <li>RESIDENTIAL PAINTERS</li>
    <li>COMMERCIAL PAINTERS</li>
    <li>OFFICE FITOUTS</li>
    <li>COLOUR CONSULTANCY</li>
    <li>PROPERTY MAINTENANCE</li>
    <li>QUALIFIED INTERIOR DESIGNER</li>
    <li style="border-bottom:none">DECORATIVE PAINT FINISHES</li>
  </ul>
  <h2 style="top:803px">Members</h2>
  <div class="abs member">Registered Member</div>
  <svg class="abs badge" viewBox="0 0 197 146" role="img" aria-label="Guild Decorators Australia member badge">
    <rect x="40" y="2" width="117" height="100" rx="10" fill="#d9d9d9"/>
    <rect x="12" y="114" width="173" height="6" fill="#cfcfcf"/>
    <rect x="12" y="127" width="173" height="6" fill="#cfcfcf"/>
    <rect x="12" y="140" width="173" height="6" fill="#cfcfcf"/>
  </svg>
  <h2 style="top:1038px">we Accept</h2>
  <div class="abs cards" style="top:1078px"><i style="width:30px"></i><i style="width:30px"></i><i style="width:30px"></i><i style="width:44px"></i></div>
  <div class="abs cards" style="top:1106px;left:745px;width:150px"><i style="width:46px;height:14px"></i><i style="width:30px;height:14px"></i><i style="width:30px;height:14px"></i></div>
</aside>

<footer class="abs footer">
  <a href="#" style="left:272px">Home Page</a>
  <span class="bar" style="left:337px"></span>
  <a href="#" style="left:396px">Residential</a>
  <span class="bar" style="left:458px"></span>
  <a href="#" style="left:523px">Commercial</a>
  <span class="bar" style="left:593px"></span>
  <a href="#" style="left:648px">Insurance</a>
  <span class="bar" style="left:707px"></span>
  <a href="#" style="left:772px">Contact Us</a>
</footer>

</body>
</html>
```